Develop A Dynamic, Professional Powerpoint Design Template

We need a dynamic powerpoint design for a new company that designs novel product packaging. We would like to see designs that use the color black and blue. The final design should communicate "change" and "transitions". See attachments for inspiration on graphics that inspire us.

We like these colors:
Black
Blue
Green
Orange

Reason: We need to extend this contest to allow for the inclusion of our final logo design which is expected to be completed tomorrow, 10/28/2015.

Target Market(s)

High end clients.

Industry/Entity Type

It Company

Font styles to use
Serif

Requirements
Must have
• See "example" slides for type of information that we will be presenting. The name of our company is "Larkspur Carton Works". This template will be used for a new company and I attach a logo concept for your consideration.

```html
<!DOCTYPE html>
<html lang="en">
<head>
<meta charset="utf-8">
<title>Larkspur Carton Works – Presentation Template</title>
<link href="https://fonts.googleapis.com/css2?family=Arimo:wght@400;700&display=swap" rel="stylesheet">
<style>
  :root {
    --stage: #6b6b6b;
    --green-deep: #0b3a1c;
    --green-mid: #13702f;
    --green-glow: #2fae3c;
    --lime: #c9e81c;
    --yellow: #f2e600;
    --brand-green: #3bb44a;
    --white: #ffffff;
    --ink: #1e1e1e;
    --paper-grey: #d9dcdc;
  }
  * { box-sizing: border-box; margin: 0; padding: 0; }
  html, body { width: 847px; height: 1200px; overflow: hidden; }
  body {
    background: var(--stage);
    font-family: "Arimo", Arial, sans-serif;
    position: relative;
  }
  .slide {
    position: absolute;
    left: 55px;
    width: 738px;
    height: 545px;
    background: var(--white);
    overflow: hidden;
  }
  .slide--title { top: 28px; }
  .slide--content { top: 622px; }
  .slide svg.backdrop { position: absolute; inset: 0; width: 100%; height: 100%; }

  /* Title slide */
  .title-block { position: absolute; left: 40px; top: 52px; color: var(--white); }
  .title-block .heading {
    font-size: 50px; font-weight: 700; color: var(--lime); letter-spacing: 0.5px;
  }
  .title-block .subheading { font-size: 25px; font-weight: 700; margin-top: 14px; }
  .title-block .tagline { font-size: 16px; line-height: 1.3; margin-top: 22px; }
  .brand-name {
    font-weight: 700; color: var(--brand-green); white-space: nowrap;
  }
  .slide--title .brand-name { position: absolute; left: 40px; top: 470px; font-size: 24px; }
  .presenter {
    position: absolute; right: 40px; top: 432px; text-align: right;
    font-size: 11px; font-weight: 700; color: var(--ink); line-height: 1.3;
  }
  .presenter .date { font-weight: 400; margin-top: 6px; }
  .web { font-size: 11px; color: var(--brand-green); }
  .slide--title .web { position: absolute; right: 40px; top: 505px; }

  /* Content slide */
  .content-head { position: absolute; left: 28px; top: 24px; }
  .content-head .heading { font-size: 28px; font-weight: 700; color: var(--white); }
  .content-head .subheading { font-size: 20px; font-weight: 700; color: var(--yellow); margin-top: 4px; }
  .slide--content .brand-name { position: absolute; right: 26px; top: 74px; font-size: 17px; }
  .footer { position: absolute; right: 26px; bottom: 18px; font-size: 11px; display: flex; gap: 10px; align-items: center; }
  .footer .page { color: var(--ink); padding-left: 8px; border-left: 1px solid #999; }
</style>
</head>
<body>

<section class="slide slide--title">
  <svg class="backdrop" viewBox="0 0 738 545" preserveAspectRatio="none">
    <defs>
      <radialGradient id="titleGlow" cx="62%" cy="48%" r="70%">
        <stop offset="0" stop-color="var(--green-glow)"/>
        <stop offset="0.45" stop-color="var(--green-mid)"/>
        <stop offset="1" stop-color="var(--green-deep)"/>
      </radialGradient>
    </defs>
    <rect width="738" height="545" fill="url(#titleGlow)" role="img" aria-label="Glowing green background with flowing light waves"/>
    <path d="M0,420 C260,430 480,410 738,330 L738,545 L0,545 Z" fill="var(--yellow)"/>
    <path d="M0,432 C260,442 480,424 738,348 L738,545 L0,545 Z" fill="var(--white)"/>
  </svg>
  <div class="title-block">
    <h1 class="heading">HEADING HERE</h1>
    <h2 class="subheading">SUBHEADING HERE</h2>
    <p class="tagline">Example Slides For New Design PPT<br>Design Template</p>
  </div>
  <div class="brand-name">Larkspur Carton Works</div>
  <div class="presenter">
    <div>NAME OF THE<br>PRESENTERE</div>
    <div class="date">Date : 00 00 00</div>
  </div>
  <div class="web">www.larkspurcarton.com</div>
</section>

<section class="slide slide--content">
  <svg class="backdrop" viewBox="0 0 738 545" preserveAspectRatio="none">
    <defs>
      <linearGradient id="headBand" x1="0" y1="0" x2="1" y2="0">
        <stop offset="0" stop-color="var(--green-deep)"/>
        <stop offset="1" stop-color="var(--green-mid)"/>
      </linearGradient>
      <linearGradient id="floorFade" x1="0" y1="0" x2="0" y2="1">
        <stop offset="0" stop-color="var(--white)"/>
        <stop offset="0.55" stop-color="#f2f3f3"/>
        <stop offset="1" stop-color="var(--paper-grey)"/>
      </linearGradient>
    </defs>
    <rect y="100" width="738" height="445" fill="url(#floorFade)" role="img" aria-label="Soft grey area with translucent glass cubes"/>
    <path d="M0,0 H738 V40 C480,42 400,102 260,110 L0,110 Z" fill="var(--yellow)"/>
    <path d="M0,0 H738 V30 C470,32 390,92 250,100 L0,100 Z" fill="url(#headBand)"/>
  </svg>
  <div class="content-head">
    <h1 class="heading">ADD YOUR HEADING HERE</h1>
    <h2 class="subheading">Add your subheading here</h2>
  </div>
  <div class="brand-name">Larkspur Carton Works</div>
  <div class="footer">
    <span class="web">www.larkspurcarton.com</span>
    <span class="page">01</span>
  </div>
</section>

</body>
</html>
```